Website and Mobile Devices design for food related application.

We need a design that is simple yet playful. The design should be food related if possible.
This design will be on the website and the mobile platform markets we intend application to be deployed too.
This application/website is called "Pickvoro[.com]. Its a random restaurant picker for the indecisive users.
Updates
Hi all, I picked a design. Again lots of great designs were submitted but I picked one that was more in line with what I wanted.
Target Market(s)
young internet savvy users.
Industry/Entity Type
Restaurant
Look and feel
Each slider illustrates characteristics of the customer's brand and the style your logo design should communicate.

```html
<!DOCTYPE html>
<html lang="en">
<head>
<meta charset="utf-8">
<title>Pickvoro – mobile screens</title>
<link href="https://fonts.googleapis.com/css2?family=Arimo:wght@400;700&display=swap" rel="stylesheet">
<style>
:root{
  --bg:#ffffff;
  --status:#111111;
  --head-top:#5d86b3;
  --head-bot:#2d5a8c;
  --seg-top:#4f7fb2;
  --seg-bot:#2c5d92;
  --seg-active-top:#e68a45;
  --seg-active-bot:#c45d1c;
  --list-bg:#f4f7fa;
  --row-line:#c9d3e3;
  --name:#0a1a8a;
  --accent:#e98a12;
  --dot-ring:#f7dcc3;
  --chevron:#c5661a;
  --tab-top:#5b8ec0;
  --tab-bot:#2f6aa3;
  --tab-active:#1f4f86;
  --tab-label:#0f2f7a;
  --white:#ffffff;
  --map-a:#f1ecdf;
  --map-b:#e9e3c8;
}
*{box-sizing:border-box;margin:0;padding:0}
html,body{width:1200px;height:1000px;overflow:hidden;background:var(--bg);font-family:"Arimo",Arial,sans-serif}
.stage{position:relative;width:1200px;height:1000px}
.screen{position:absolute;top:298px;width:288px;height:430px;background:var(--list-bg);overflow:hidden;display:flex;flex-direction:column}
.screen--list{left:36px}
.screen--map{left:453px}
.screen--favs{left:873px}

.status-bar{height:20px;background:var(--status);color:var(--white);font-size:11px;font-weight:700;display:flex;align-items:center;padding:0 6px;position:relative}
.status-bar .signal{display:flex;align-items:flex-end;gap:1px;margin-right:3px}
.status-bar .signal i{display:block;width:2px;background:var(--white)}
.status-bar .clock{position:absolute;left:0;right:0;text-align:center;font-size:12px}
.status-bar .battery{margin-left:auto;width:20px;height:9px;border:1px solid #ddd;border-radius:2px;padding:1px}
.status-bar .battery b{display:block;height:100%;background:#ddd}

.top-bar{height:36px;background:linear-gradient(var(--head-top),var(--head-bot));display:flex;align-items:center;padding:0 6px;gap:6px}
.search-field{flex:1;height:25px;background:var(--white);border-radius:13px;display:flex;align-items:center;padding:0 8px 0 6px;font-size:13px;color:#111;gap:6px}
.search-field .divider{width:1px;height:17px;background:#bbb}
.search-field .brand-dot{margin-left:auto;width:12px;height:12px;border-radius:50%;background:var(--accent)}

.segments{height:29px;display:flex;background:linear-gradient(var(--seg-top),var(--seg-bot));border-top:1px solid #7fa3c8}
.segments span{flex:1;display:flex;align-items:center;justify-content:center;color:var(--white);font-size:12px;border-right:1px solid #254d7a}
.segments span:last-child{border-right:0}
.segments .is-active{background:linear-gradient(var(--seg-active-top),var(--seg-active-bot))}

.restaurant-list{flex:1;list-style:none;overflow:hidden}
.restaurant{height:53px;border-bottom:1px solid var(--row-line);position:relative;display:flex;align-items:center}
.restaurant .marker{position:absolute;left:8px;width:21px;height:21px;border-radius:50%;background:var(--dot-ring);display:flex;align-items:center;justify-content:center}
.restaurant .marker::after{content:"";width:9px;height:9px;border-radius:50%;background:var(--accent)}
.restaurant .name{position:absolute;left:63px;top:8px;color:var(--name);font-size:14px}
.restaurant .meta{position:absolute;left:63px;top:27px;width:160px;font-size:10px;font-weight:700;color:var(--accent)}
.restaurant .price{position:absolute;left:90px;top:0}
.restaurant .dist{position:absolute;left:150px;top:0}
.restaurant .chevron{position:absolute;right:8px;top:19px}

.map-view{flex:1;background:radial-gradient(circle at 40% 60%,#cfd9c0 0,transparent 28%),linear-gradient(135deg,var(--map-a),var(--map-b))}

.tab-bar{height:40px;background:linear-gradient(var(--tab-top),var(--tab-bot));display:flex}
.tab{flex:1;display:flex;flex-direction:column;align-items:center;justify-content:flex-end;padding-bottom:2px;font-size:9px;color:var(--tab-label)}
.tab svg{margin-bottom:2px}
.tab.is-active{background:var(--tab-active);color:var(--accent);font-weight:700}
</style>
</head>
<body>
<div class="stage">

  <!-- list screen -->
  <section class="screen screen--list">
    <div class="status-bar"><span class="signal"><i style="height:3px"></i><i style="height:5px"></i><i style="height:7px"></i><i style="height:9px"></i></span>Mobile<span class="clock">6:40 PM</span><span class="battery"><b></b></span></div>
    <div class="top-bar">
      <svg width="16" height="16" viewBox="0 0 16 16" fill="none" stroke="#fff" stroke-width="2"><path d="M13 6a5.5 5.5 0 0 0-10 0M3 10a5.5 5.5 0 0 0 10 0"/><path d="M13 2v4H9M3 14v-4h4" stroke-width="1.6"/></svg>
      <div class="search-field"><svg width="13" height="13" viewBox="0 0 13 13" fill="none" stroke="#444" stroke-width="1.8"><circle cx="5.5" cy="5.5" r="4"/><path d="M8.5 8.5l3.5 3.5"/></svg><span class="divider"></span>Pickvoro<span class="brand-dot"></span></div>
    </div>
    <nav class="segments"><span class="is-active">Distance</span><span>Cuisine</span><span>Random</span></nav>
    <ul class="restaurant-list">
      <li class="restaurant"><span class="marker"></span><span class="name">Name Of Restaurant 1</span><span class="meta">Chinese<span class="price">$</span><span class="dist">99m</span></span><svg class="chevron" width="9" height="14" viewBox="0 0 9 14"><path d="M1 1l6 6-6 6" fill="none" stroke="#c5661a" stroke-width="2"/></svg></li>
      <li class="restaurant"><span class="marker"></span><span class="name">Name Of Restaurant 2</span><span class="meta">French<span class="price">$$$</span><span class="dist">100m</span></span><svg class="chevron" width="9" height="14" viewBox="0 0 9 14"><path d="M1 1l6 6-6 6" fill="none" stroke="#c5661a" stroke-width="2"/></svg></li>
      <li class="restaurant"><span class="marker"></span><span class="name">Name Of Restaurant 3</span><span class="meta">American<span class="price">$</span><span class="dist">160m</span></span><svg class="chevron" width="9" height="14" viewBox="0 0 9 14"><path d="M1 1l6 6-6 6" fill="none" stroke="#c5661a" stroke-width="2"/></svg></li>
      <li class="restaurant"><span class="marker"></span><span class="name">Name Of Restaurant 1</span><span class="meta">Japanese<span class="price">$$$</span><span class="dist">99m</span></span><svg class="chevron" width="9" height="14" viewBox="0 0 9 14"><path d="M1 1l6 6-6 6" fill="none" stroke="#c5661a" stroke-width="2"/></svg></li>
      <li class="restaurant"><span class="marker"></span><span class="name">Name Of Restaurant 1</span><span class="meta">Moroccan<span class="price">$$</span><span class="dist">50m</span></span><svg class="chevron" width="9" height="14" viewBox="0 0 9 14"><path d="M1 1l6 6-6 6" fill="none" stroke="#c5661a" stroke-width="2"/></svg></li>
      <li class="restaurant"><span class="marker"></span><span class="name">Name Of Restaurant 1</span><span class="meta">Italien<span class="price">$$$</span><span class="dist">200m</span></span><svg class="chevron" width="9" height="14" viewBox="0 0 9 14"><path d="M1 1l6 6-6 6" fill="none" stroke="#c5661a" stroke-width="2"/></svg></li>
    </ul>
    <nav class="tab-bar">
      <span class="tab is-active"><svg width="14" height="18" viewBox="0 0 14 18"><path d="M7 1a6 6 0 0 0-6 6c0 4 6 10 6 10s6-6 6-10a6 6 0 0 0-6-6z" fill="#fff"/><circle cx="7" cy="7" r="2.2" fill="#1f4f86"/></svg>Stations</span>
      <span class="tab"><svg width="16" height="16" viewBox="0 0 16 16"><path d="M1 3l4-2 6 2 4-2v12l-4 2-6-2-4 2z" fill="#fff"/></svg>Map</span>
      <span class="tab"><svg width="18" height="17" viewBox="0 0 18 17"><path d="M9 0l2.6 5.6 6 .6-4.6 4 1.4 6L9 13l-5.4 3.2 1.4-6-4.6-4 6-.6z" fill="#fff"/></svg>Favoris</span>
      <span class="tab"><svg width="20" height="14" viewBox="0 0 20 14"><rect x="0.5" y="0.5" width="19" height="13" rx="1.5" fill="#fff"/><rect x="0.5" y="3" width="19" height="3" fill="#222"/></svg>Reservation</span>
      <span class="tab"><svg width="16" height="16" viewBox="0 0 16 16"><path d="M3 1l3 3-1.5 2a9 9 0 0 0 5.5 5.5l2-1.5 3 3-2 2C7 15 1 9 1 3z" fill="#fff"/></svg>Contact</span>
    </nav>
  </section>

  <!-- map screen -->
  <section class="screen screen--map">
    <div class="status-bar"><span class="signal"><i style="height:3px"></i><i style="height:5px"></i><i style="height:7px"></i><i style="height:9px"></i></span>Mobile<span class="clock">6:40 PM</span><span class="battery"><b></b></span></div>
    <div class="top-bar">
      <svg width="16" height="16" viewBox="0 0 16 16" fill="none" stroke="#fff" stroke-width="2"><path d="M13 6a5.5 5.5 0 0 0-10 0M3 10a5.5 5.5 0 0 0 10 0"/><path d="M13 2v4H9M3 14v-4h4" stroke-width="1.6"/></svg>
      <div class="search-field"><svg width="13" height="13" viewBox="0 0 13 13" fill="none" stroke="#444" stroke-width="1.8"><circle cx="5.5" cy="5.5" r="4"/><path d="M8.5 8.5l3.5 3.5"/></svg><span class="divider"></span>Pickvoro<span class="brand-dot"></span></div>
    </div>
    <nav class="segments"><span class="is-active">Distance</span><span>Cuisine</span><span>Random</span></nav>
    <div class="map-view" role="img" aria-label="City street map with restaurant location pins"></div>
    <nav class="tab-bar">
      <span class="tab"><svg width="14" height="18" viewBox="0 0 14 18"><path d="M7 1a6 6 0 0 0-6 6c0 4 6 10 6 10s6-6 6-10a6 6 0 0 0-6-6z" fill="#fff"/><circle cx="7" cy="7" r="2.2" fill="#2f6aa3"/></svg>Stations</span>
      <span class="tab is-active"><svg width="16" height="16" viewBox="0 0 16 16"><path d="M1 3l4-2 6 2 4-2v12l-4 2-6-2-4 2z" fill="#fff"/></svg>Map</span>
      <span class="tab"><svg width="18" height="17" viewBox="0 0 18 17"><path d="M9 0l2.6 5.6 6 .6-4.6 4 1.4 6L9 13l-5.4 3.2 1.4-6-4.6-4 6-.6z" fill="#fff"/></svg>Favoris</span>
      <span class="tab"><svg width="20" height="14" viewBox="0 0 20 14"><rect x="0.5" y="0.5" width="19" height="13" rx="1.5" fill="#fff"/><rect x="0.5" y="3" width="19" height="3" fill="#222"/></svg>Reservation</span>
      <span class="tab"><svg width="16" height="16" viewBox="0 0 16 16"><path d="M3 1l3 3-1.5 2a9 9 0 0 0 5.5 5.5l2-1.5 3 3-2 2C7 15 1 9 1 3z" fill="#fff"/></svg>Contact</span>
    </nav>
  </section>

  <!-- favourites screen -->
  <section class="screen screen--favs">
    <div class="status-bar"><span class="signal"><i style="height:3px"></i><i style="height:5px"></i><i style="height:7px"></i><i style="height:9px"></i></span>Mobile<span class="clock">6:40 PM</span><span class="battery"><b></b></span></div>
    <div class="top-bar">
      <svg width="16" height="16" viewBox="0 0 16 16" fill="none" stroke="#fff" stroke-width="2"><path d="M13 6a5.5 5.5 0 0 0-10 0M3 10a5.5 5.5 0 0 0 10 0"/><path d="M13 2v4H9M3 14v-4h4" stroke-width="1.6"/></svg>
      <div class="search-field"><svg width="13" height="13" viewBox="0 0 13 13" fill="none" stroke="#444" stroke-width="1.8"><circle cx="5.5" cy="5.5" r="4"/><path d="M8.5 8.5l3.5 3.5"/></svg><span class="divider"></span>Pickvoro<span class="brand-dot"></span></div>
    </div>
    <nav class="segments"><span class="is-active">Distance</span><span>Cuisine</span><span>Random</span></nav>
    <ul class="restaurant-list">
      <li class="restaurant"><span class="marker"></span><span class="name">Name Of Restaurant 1</span><span class="meta">Chinese<span class="price">$</span><span class="dist">99m</span></span><svg class="chevron" width="9" height="14" viewBox="0 0 9 14"><path d="M1 1l6 6-6 6" fill="none" stroke="#c5661a" stroke-width="2"/></svg></li>
      <li class="restaurant"><span class="marker"></span><span class="name">Name Of Restaurant 2</span><span class="meta">French<span class="price">$$$</span><span class="dist">100m</span></span><svg class="chevron" width="9" height="14" viewBox="0 0 9 14"><path d="M1 1l6 6-6 6" fill="none" stroke="#c5661a" stroke-width="2"/></svg></li>
      <li class="restaurant"><span class="marker"></span><span class="name">Name Of Restaurant 3</span><span class="meta">American<span class="price">$</span><span class="dist">160m</span></span><svg class="chevron" width="9" height="14" viewBox="0 0 9 14"><path d="M1 1l6 6-6 6" fill="none" stroke="#c5661a" stroke-width="2"/></svg></li>
    </ul>
    <nav class="tab-bar">
      <span class="tab"><svg width="14" height="18" viewBox="0 0 14 18"><path d="M7 1a6 6 0 0 0-6 6c0 4 6 10 6 10s6-6 6-10a6 6 0 0 0-6-6z" fill="#fff"/><circle cx="7" cy="7" r="2.2" fill="#2f6aa3"/></svg>Stations</span>
      <span class="tab"><svg width="16" height="16" viewBox="0 0 16 16"><path d="M1 3l4-2 6 2 4-2v12l-4 2-6-2-4 2z" fill="#fff"/></svg>Map</span>
      <span class="tab is-active"><svg width="18" height="17" viewBox="0 0 18 17"><path d="M9 0l2.6 5.6 6 .6-4.6 4 1.4 6L9 13l-5.4 3.2 1.4-6-4.6-4 6-.6z" fill="#fff"/></svg>Favoris</span>
      <span class="tab"><svg width="20" height="14" viewBox="0 0 20 14"><rect x="0.5" y="0.5" width="19" height="13" rx="1.5" fill="#fff"/><rect x="0.5" y="3" width="19" height="3" fill="#222"/></svg>Reservation</span>
      <span class="tab"><svg width="16" height="16" viewBox="0 0 16 16"><path d="M3 1l3 3-1.5 2a9 9 0 0 0 5.5 5.5l2-1.5 3 3-2 2C7 15 1 9 1 3z" fill="#fff"/></svg>Contact</span>
    </nav>
  </section>

</div>
</body>
</html>
```